Labels for my sauce bottles

I have designed the label- a few change suggestions are welcome<br/>but I basically need what is on the uploaded images- made high quality<br/>I don't have the programs to ensure it prints correctly and doesn't blur.<br/>I also have more labels to do- name, barcode and Nutritional Panel change- design/ concept stay the same<br/>dimensions are 190mm (long) x 75mm (High)

Font styles to use
Decorative
Script

Colors
ffc214

```html
<!DOCTYPE html>
<html lang="en">
<head>
<meta charset="utf-8">
<title>Ember Bloom – Pumpkin Blaze label</title>
<link href="https://fonts.googleapis.com/css2?family=Barlow+Condensed:wght@400;500;600&family=Baloo+2:wght@600&family=Yellowtail&display=swap" rel="stylesheet">
<style>
  :root {
    --page: #f4f4f2;
    --board: #1d1d1d;
    --board-light: #2b2b2b;
    --gold: #b08612;
    --gold-bright: #ffc214;
    --white: #ffffff;
    --ink: #111111;
  }
  * { box-sizing: border-box; margin: 0; padding: 0; }
  html, body { width: 1200px; height: 1141px; overflow: hidden; background: var(--page); }
  body { position: relative; font-family: "Barlow Condensed", sans-serif; }

  .label {
    position: absolute; left: 20px; top: 332px; width: 1160px; height: 476px;
    background: radial-gradient(ellipse at 60% 35%, var(--board-light), var(--board) 70%);
    color: var(--white);
  }

  .ingredients { position: absolute; left: 41px; top: 36px; width: 220px; }
  .ingredients__title { font-family: "Baloo 2", sans-serif; font-weight: 600; color: var(--gold); font-size: 19px; letter-spacing: .5px; }
  .ingredients__list { font-size: 18px; line-height: 23px; margin-top: 6px; }

  .notes { position: absolute; left: 37px; top: 186px; width: 206px; text-align: center; font-size: 16px; line-height: 19px; }
  .notes__additives { color: var(--gold); }

  .nutrition {
    position: absolute; left: 37px; top: 222px; width: 206px; height: 204px;
    background: var(--white); color: var(--ink); border: 2px solid var(--white);
    outline: 1.5px solid var(--ink); outline-offset: -4px; padding: 8px 9px; font-size: 9.5px; line-height: 13px;
  }
  .nutrition__title { font-weight: 600; font-size: 13px; letter-spacing: 2.6px; padding-left: 4px; margin-bottom: 5px; }
  .nutrition__meta { display: grid; grid-template-columns: 86px 1fr; padding-left: 4px; }
  .nutrition__rule { border-top: 1px solid var(--ink); margin: 6px -5px 2px; }
  .nutrition__head, .nutrition__row { display: grid; grid-template-columns: 86px 38px 16px 26px 16px; padding-left: 4px; }
  .nutrition__head span { grid-column: span 2; line-height: 12px; }
  .nutrition__head span:first-child { grid-column: 2 / span 2; }
  .nutrition__rows { margin-top: 4px; }
  .num { text-align: right; padding-right: 4px; }

  .footnote { position: absolute; left: 37px; top: 450px; width: 206px; text-align: center; font-size: 15px; }

  .tagline { position: absolute; left: 0; right: 0; top: 60px; text-align: center; font-family: "Yellowtail", cursive; font-size: 32px; color: var(--gold); }
  .brand { position: absolute; left: 0; right: 0; top: 168px; display: flex; justify-content: center; align-items: center; gap: 22px; }
  .brand__mark { width: 26px; height: 26px; border-radius: 50%; background: var(--gold-bright); }
  .brand__name { font-family: "Yellowtail", cursive; font-size: 92px; line-height: 1; color: var(--white); }
  .product { position: absolute; left: 0; right: 0; top: 318px; text-align: center; font-family: "Baloo 2", sans-serif; font-weight: 600; font-size: 64px; line-height: 1; color: var(--gold); }
  .volume { position: absolute; left: 0; right: 0; top: 420px; text-align: center; font-size: 22px; font-weight: 500; }

  .maker { position: absolute; left: 983px; top: 26px; font-size: 15.5px; line-height: 20px; letter-spacing: .8px; }
  .batch { position: absolute; left: 983px; top: 364px; font-size: 12px; line-height: 30px; }
  .website { position: absolute; left: 983px; top: 428px; font-size: 17px; letter-spacing: 1.6px; }
</style>
</head>
<body>
  <section class="label">
    <div class="ingredients">
      <h2 class="ingredients__title">Ingredients:</h2>
      <p class="ingredients__list">Pumpkin, Coconut Cream, Vinegar, Habaneros, Fatalii Medley, Butter, Garlic, Peppercorns, Salt</p>
    </div>
    <div class="notes" style="top:188px">
      <p class="notes__additives">No Artificial Additives</p>
      <p>Refrigerate after opening</p>
    </div>

    <div class="nutrition" style="top:242px">
      <p class="nutrition__title">NUTRITION INFORMATION</p>
      <div class="nutrition__meta"><span>Servings per package:</span><span>16.60</span><span>Serving Size:</span><span>15.00 ml</span></div>
      <div class="nutrition__rule"></div>
      <div class="nutrition__head"><span>Average Quantity per Serving</span><span>Average Quantity per 100 ml</span></div>
      <div class="nutrition__rule"></div>
      <div class="nutrition__rows">
        <div class="nutrition__row"><span>Energy</span><span class="num">79</span><span>kJ</span><span class="num">529</span><span>kJ</span></div>
        <div class="nutrition__row"><span>Protein</span><span class="num">0.5</span><span>g</span><span class="num">3.4</span><span>g</span></div>
        <div class="nutrition__row"><span>Fat, total</span><span class="num">1.3</span><span>g</span><span class="num">8.6</span><span>g</span></div>
        <div class="nutrition__row"><span>-saturated</span><span class="num">1.0</span><span>g</span><span class="num">6.9</span><span>g</span></div>
        <div class="nutrition__row"><span>Carbohydrate</span><span class="num">1.4</span><span>g</span><span class="num">9.7</span><span>g</span></div>
        <div class="nutrition__row"><span>-sugars</span><span class="num">1.0</span><span>g</span><span class="num">6.4</span><span>g</span></div>
        <div class="nutrition__row"><span>Sodium</span><span class="num">24</span><span>mg</span><span class="num">162</span><span>mg</span></div>
      </div>
    </div>
    <p class="footnote">* Average daily adult intake</p>

    <p class="tagline">small batch craft sauce</p>
    <div class="brand">
      <span class="brand__name">Ember Bloom</span>
      <span class="brand__mark"></span>
    </div>
    <h1 class="product">Pumpkin Blaze</h1>
    <p class="volume">250 ml</p>

    <p class="maker">Produced and Bottled<br>on the Sunshine Coast</p>
    <div class="batch"><p>Batch Number:</p><p>Best Before:</p></div>
    <p class="website">emberbloom.com.au</p>
  </section>
</body>
</html>
```